Financial Planning Business needs a business card design

We need a business card design that is for a new financial planning business based in Australia. We provide financial planning advice such as retirement planning, wealth creation, asset protection.

Attached is the logo design. On the front side of the business card needs to incorporate the following:
- adviser name
- adviser title (ie Managing Director)
- address
- phone number
- email
- website address

Ideally it should also have the business name and logo

On the back of the card I would like this to be black in colour with the business name and logo

I have been advised the font is "Cinzel" (regular and bold)

Industry/Entity Type

Financial

Requirements
Must have
• Logo and business name

Format to have as follows:
Ben xxxxxxxx
Managing Director / Senior Financial Adviser
address
phone email
website

```html
<!DOCTYPE html>
<html lang="en">
<head>
<meta charset="utf-8">
<title>Kestrel Advisory – Business Card</title>
<link rel="stylesheet" href="https://fonts.googleapis.com/css2?family=Cinzel:wght@400&family=Open+Sans:wght@400;600&display=swap">
<style>
  :root {
    --teal: #2fb3dc;
    --teal-deep: #1a7fa3;
    --ink: #222427;
    --grey-light: #c9cbce;
    --paper: #ffffff;
    --stage: #ecebe8;
    --card-black: #141516;
  }
  * { box-sizing: border-box; margin: 0; padding: 0; }
  html, body { width: 1200px; height: 1023px; overflow: hidden; }
  body {
    background: var(--stage);
    display: flex;
    flex-direction: column;
    align-items: center;
    justify-content: center;
    gap: 70px;
    font-family: "Open Sans", sans-serif;
  }
  .card {
    position: relative;
    width: 640px;
    height: 366px;
    overflow: hidden;
    box-shadow: 0 10px 30px rgba(0,0,0,.18);
  }

  /* Front */
  .card-front { background: var(--paper); }
  .front-panel {
    position: absolute; top: 0; right: 0; width: 210px; height: 310px;
    background: linear-gradient(160deg, #e6e7e9 0%, #a9abae 55%, #3a3c3f 100%);
  }
  .front-accent {
    position: absolute; top: 150px; right: 0; width: 34px; height: 120px;
    background: var(--teal);
  }
  .brand {
    position: absolute; left: 40px; top: 52px;
    display: flex; align-items: center; gap: 14px;
  }
  .brand-square { width: 26px; height: 26px; background: var(--grey-light); }
  .brand-name {
    font-family: "Open Sans", sans-serif; font-weight: 600;
    color: var(--teal); font-size: 30px; line-height: 1;
  }
  .adviser { position: absolute; left: 40px; top: 150px; }
  .adviser-name {
    font-family: "Cinzel", serif; font-size: 25px; color: var(--teal);
    letter-spacing: 1px;
  }
  .adviser-title { font-size: 13px; color: var(--ink); margin-top: 2px; }
  .contacts { position: absolute; left: 40px; top: 218px; list-style: none; }
  .contacts li {
    display: flex; align-items: center; gap: 10px;
    font-size: 14px; color: var(--ink); height: 22px;
  }
  .contact-icon { width: 13px; height: 13px; }
  .address-band {
    position: absolute; left: 0; bottom: 0; width: 100%; height: 38px;
    background: linear-gradient(90deg, #2a2c2f, #151617);
    display: flex; align-items: center; padding-left: 40px;
    color: var(--teal); font-size: 14px;
  }

  /* Back */
  .card-back {
    background: linear-gradient(135deg, #3c3e41 0%, var(--card-black) 45%, #2b2d30 100%);
  }
  .back-accent {
    position: absolute; left: 0; top: 0; width: 120px; height: 366px;
    background: linear-gradient(180deg, var(--teal-deep), #0d3f52);
    clip-path: polygon(0 0, 100% 40%, 100% 100%, 0 100%);
  }
  .back-brand {
    position: absolute; inset: 0;
    display: flex; align-items: center; justify-content: center;
    padding-left: 60px;
  }
  .back-brand .brand-name { font-size: 44px; }
</style>
</head>
<body>

<section class="card card-front" aria-label="Card front">
  <div class="front-panel" role="img" aria-label="Decorative grey block area"></div>
  <div class="front-accent"></div>

  <div class="brand">
    <div class="brand-square"></div>
    <div class="brand-name">Kestrel Advisory</div>
  </div>

  <div class="adviser">
    <div class="adviser-name">Mara Ellison</div>
    <div class="adviser-title">Director</div>
  </div>

  <ul class="contacts">
    <li>
      <svg class="contact-icon" viewBox="0 0 14 14"><rect width="14" height="14" rx="2" fill="var(--teal)"/><rect x="5" y="3" width="4" height="8" rx="1" fill="#fff"/></svg>
      0412555018
    </li>
    <li>
      <svg class="contact-icon" viewBox="0 0 14 14"><rect width="14" height="14" rx="2" fill="var(--teal)"/><rect x="3" y="4" width="8" height="6" fill="#fff"/><path d="M3 4 L7 8 L11 4" stroke="var(--teal)" fill="none"/></svg>
      mara@kestreladvisory.com
    </li>
    <li>
      <svg class="contact-icon" viewBox="0 0 14 14"><rect width="14" height="14" rx="2" fill="var(--teal)"/><circle cx="7" cy="7" r="4" fill="none" stroke="#fff"/><line x1="3" y1="7" x2="11" y2="7" stroke="#fff"/></svg>
      www.kestreladvisory.com
    </li>
  </ul>

  <div class="address-band">148B Harbour View Road Unit 22, Carlton, VIC 3053</div>
</section>

<section class="card card-back" aria-label="Card back">
  <div class="back-accent"></div>
  <div class="back-brand">
    <div class="brand-name">Kestrel Advisory</div>
  </div>
</section>

</body>
</html>
```